Premium Food Label Design – High-End Boutique Jar Labels (3 Sizes)

I require a complete jar label redesign across three sizes:
75mm x 130mm (Large & Medium)
55mm x 120mm (Small)
45mm x 120mm (XS)

The design must feel professional, modern, elegant, and high-end boutique.
Primary aesthetic: white, minimal, refined, with accents in soft brown and gold/bronze. (see prefer colours of logo in OLD LABEL PDF)
Transparent background required.

I have attached my current label for wording reference only — I want to move away from the kraft look entirely.
The label must include all existing details, plus a dedicated space to manually add batch number and date.

IMPORTANT: Final files must be supplied as editable Adobe Illustrator (.AI) files with live text layers (not outlined) so I can update them as needed.
Logo is attached. I’m open to a fresh, elevated design direction aligned with a premium brand feel.
Updates

Low design quality

Target Market(s)

People who appreciate high-end, thoughtfully crafted food and are willing to pay for quality

Industry/Entity Type

Gourmet Food / Artisan Food Packaging

Requirements
Must have
• Premium, minimal aesthetic, Strong typography hierarchy, White background, Consistency across 3 sizes
Nice to have
• Elevated “Amber Meadow” styling
Should not have
• No bright or bold colours, No clutter or overcrowding, No heavy borders or thick frames,No “homemade/craft” fonts

```html
<!DOCTYPE html>
<html lang="en">
<head>
<meta charset="utf-8">
<title>Tomato Relish – Jar Labels</title>
<link href="https://fonts.googleapis.com/css2?family=Marcellus&family=Alegreya+Sans:wght@400;700&display=swap" rel="stylesheet">
<style>
  :root {
    --paper: #ffffff;
    --canvas: #ffffff;
    --brown: #3f2216;
    --olive: #66753a;
    --rule: #8a8a7a;
    --shadow: rgba(0, 0, 0, 0.16);
  }
  * { box-sizing: border-box; margin: 0; padding: 0; }
  html, body { width: 920px; height: 1200px; overflow: hidden; background: var(--canvas); }
  .artboard { position: relative; width: 920px; height: 1200px; }

  .label {
    position: absolute;
    width: 334px;
    height: 580px;
    background: var(--paper);
    box-shadow: 0 4px 14px var(--shadow);
    color: var(--brown);
    font-family: "Alegreya Sans", sans-serif;
  }
  .label--front { left: 107px; top: 123px; }
  .label--back  { left: 493px; top: 476px; }

  /* Front */
  .product-title {
    position: absolute; top: 66px; left: 0; right: 0;
    text-align: center;
    font-family: "Marcellus", serif;
    font-weight: 400;
    font-size: 53px;
    line-height: 58px;
    letter-spacing: 1px;
  }
  .stem-rule {
    position: absolute; left: 166px; top: 204px;
    width: 1.5px; height: 81px; background: var(--olive);
  }
  .brand-lockup {
    position: absolute; top: 360px; left: 0; right: 0;
    display: flex; align-items: center; justify-content: center; gap: 10px;
  }
  .brand-dot { width: 12px; height: 12px; border-radius: 50%; background: var(--olive); }
  .brand-name {
    font-family: "Alegreya Sans", sans-serif;
    font-weight: 400; font-size: 22px; letter-spacing: 3px;
    text-transform: uppercase; color: var(--brown);
  }
  .tagline {
    position: absolute; top: 463px; left: 0; right: 0;
    text-align: center; font-weight: 700; font-size: 15px;
  }
  .net-weight {
    position: absolute; top: 492px; left: 0; right: 0;
    text-align: center; font-family: "Marcellus", serif;
    font-size: 28px; color: var(--olive);
  }

  /* Back */
  .intention-title {
    position: absolute; top: 52px; left: 0; right: 0;
    text-align: center; font-family: "Marcellus", serif;
    font-weight: 400; font-size: 22px; letter-spacing: 1px;
  }
  .intention-rule {
    position: absolute; top: 91px; left: 126px;
    width: 82px; height: 1.5px; background: var(--olive);
  }
  .intention-text {
    position: absolute; top: 104px; left: 40px; right: 40px;
    text-align: center; font-size: 15px; line-height: 22px;
  }
  .divider {
    position: absolute; top: 238px; left: 36px; right: 36px;
    height: 18px; display: flex; align-items: center; justify-content: space-between;
  }
  .divider-line { width: 82px; height: 1.5px; background: var(--olive); }
  .divider-mark { width: 14px; height: 14px; border-radius: 50%; background: var(--olive); }
  .details {
    position: absolute; top: 278px; left: 36px; right: 36px;
    font-size: 15px; line-height: 22px;
  }
  .details strong { font-weight: 700; }
  .record-fields {
    position: absolute; top: 438px; left: 36px; right: 36px;
    display: flex; justify-content: space-between; font-size: 15px; font-weight: 700;
  }
  .record-field { display: flex; align-items: baseline; gap: 6px; }
  .record-blank { display: inline-block; width: 76px; border-bottom: 1px solid var(--rule); transform: translateY(-4px); }
  .maker {
    position: absolute; top: 477px; left: 36px; right: 20px;
    font-size: 13px; line-height: 16px;
  }
  .maker-name { font-weight: 700; margin-bottom: 3px; }
</style>
</head>
<body>
<main class="artboard">

  <section class="label label--front" aria-label="Front label">
    <h1 class="product-title">TOMATO<br>RELISH</h1>
    <div class="stem-rule"></div>
    <div class="brand-lockup">
      <span class="brand-dot"></span>
      <span class="brand-name">Hearth Sown</span>
    </div>
    <p class="tagline">Made with love</p>
    <p class="net-weight">375g</p>
  </section>

  <section class="label label--back" aria-label="Back label">
    <h2 class="intention-title">AMBER MEADOW</h2>
    <div class="intention-rule"></div>
    <p class="intention-text">What is made with love is felt in return. May this relish nourish more than the meal — bringing comfort, connection, and joy to every moment shared.</p>
    <div class="divider">
      <span class="divider-line"></span>
      <span class="divider-mark"></span>
      <span class="divider-line"></span>
    </div>
    <div class="details">
      <p><strong>Ingredients:</strong> Tomatoes, onion, sugar, vinegar, salt, spices, thickener (cornflour)</p>
      <p><strong>Storage:</strong> Keep refrigerated once opened</p>
    </div>
    <div class="record-fields">
      <span class="record-field">Batch: <span class="record-blank"></span></span>
      <span class="record-field">Date: <span class="record-blank"></span></span>
    </div>
    <div class="maker">
      <p class="maker-name">Made by Hearth Sown, QLD, Australia</p>
      <p>W: hearthsown.com</p>
      <p>E: info@hearthsown.com</p>
    </div>
  </section>

</main>
</body>
</html>
```